Company: Plant Grillhouse
We make Plant Grillhouse more popular.
We are producing cooking books and spices.
For our spices (5 sorts) we need an label design.
Measurments of the label: 255mm x 55mm ( small changes of the exact measurements could follow in the next few days)
Name of the sorts:
- Sunny Zestpepper (Yellow)
- Desert Caravan (Orange/Brown)
- Charred Ember-Rub (Red)
- Charm of Tuscany (Green)
- Bold Shallotine (Black)
Attached you can find our main brand.
You can see we try to be clean and simple.
The package is a square glass with a cork closure
4 Side.
Side 1: Logo and Spice Name
Side 2: Incredients and Company Information
Side 3: Nice grphic that matches the sort of the spice
Side 4: Short story of the product and its added value
We look forward to cool suggestions.
Regards
Tobias
We want make the vegan lifestyle more cool.
So therefore don`t choose a too much ecological way, that is not up to date.

```html
<!DOCTYPE html>
<html lang="de">
<head>
<meta charset="utf-8">
<title>Sunny Zestpepper – Etikett</title>
<link href="https://fonts.googleapis.com/css2?family=Anton&family=Didact+Gothic&family=Montserrat:wght@700&display=swap" rel="stylesheet">
<style>
  :root {
    --label-yellow: #fdd647;
    --ink: #111111;
    --band-black: #000000;
    --divider-white: #ffffff;
    --art-light: #f3d77a;
    --art-dark: #8a7a3c;
  }
  * { margin: 0; padding: 0; box-sizing: border-box; }
  html, body { width: 1200px; height: 259px; overflow: hidden; background: var(--label-yellow); }
  .label { position: relative; width: 1200px; height: 259px; background: var(--label-yellow); color: var(--ink); }

  .herb-art {
    position: absolute; left: 0; top: 0; width: 376px; height: 209px;
    background: linear-gradient(120deg, var(--art-light) 0%, #e9cb62 45%, var(--art-dark) 100%);
    opacity: .55;
  }
  .herb-art--edge {
    left: auto; right: 0; top: 40px; width: 30px; height: 90px;
    border-radius: 30px 0 0 30px;
  }

  .spice-name {
    position: absolute; left: 400px; top: 30px; width: 176px;
    font-family: "Anton", sans-serif; font-size: 56px; line-height: 54px;
    letter-spacing: .2em; text-align: center; text-transform: uppercase;
    padding-left: .2em;
  }

  .story, .ingredients { position: absolute; top: 24px; text-align: center; }
  .story { left: 644px; width: 250px; }
  .ingredients { left: 965px; width: 200px; }

  .section-title {
    font-family: "Montserrat", sans-serif; font-weight: 700; font-size: 10.5px;
    letter-spacing: .18em; text-transform: uppercase; margin-bottom: 16px;
  }
  .story-text {
    font-family: "Didact Gothic", sans-serif; font-size: 11px; line-height: 16.1px;
    letter-spacing: .12em;
  }

  .nutrition { list-style: none; font-family: "Didact Gothic", sans-serif; font-size: 11.5px; line-height: 16px; letter-spacing: .12em; text-transform: uppercase; }
  .nutrition li { display: flex; align-items: baseline; }
  .nutrition .leader { flex: 1; border-bottom: 1.5px dotted var(--ink); margin: 0 2px 3px; }

  .company {
    margin-top: 20px;
    font-family: "Montserrat", sans-serif; font-weight: 700; font-size: 10.5px;
    letter-spacing: .16em; text-transform: uppercase;
  }

  .divider { position: absolute; left: 0; top: 209px; width: 100%; height: 3px; background: var(--divider-white); }
  .brand-band {
    position: absolute; left: 0; top: 212px; width: 100%; height: 45px; background: var(--band-black);
    display: flex; align-items: center;
  }
  .brand {
    position: absolute; left: 398px; top: 50%; transform: translateY(-50%);
    display: flex; align-items: center; gap: 10px;
    font-family: "Montserrat", sans-serif; font-weight: 700; font-size: 14px; color: var(--divider-white);
  }
  .brand-dot { width: 22px; height: 22px; border-radius: 50%; background: var(--divider-white); }
</style>
</head>
<body>
<main class="label">
  <div class="herb-art" role="img" aria-label="Hand-drawn illustration of basil, chili peppers, garlic, seeds and rosemary"></div>
  <div class="herb-art herb-art--edge" role="img" aria-label="Edge of a hand-drawn basil leaf illustration"></div>

  <h1 class="spice-name">Sunny<br>Zest<br>Pepper</h1>

  <section class="story">
    <h2 class="section-title">Zestpepper-Gewürz:</h2>
    <p class="story-text">Geschichte des Gewürzes. Lorem ipsum dolor sit amet, consetetur sadipscing elitr, sed diam nonumy eirmod tempor invidunt ut labore et dolore magna aliquyam erat, sed diam voluptua.<br>sed diam nonumy eirmod tempor invidunt ut magna aliquyam erat, sed diam voluptua</p>
  </section>

  <section class="ingredients">
    <h2 class="section-title">Inhaltsstoffe:</h2>
    <ul class="nutrition">
      <li>Energie<span class="leader"></span>kJ/kcal</li>
      <li>Fett<span class="leader"></span>g</li>
      <li>Kohlenhydrate<span class="leader"></span>g</li>
      <li>davon Zucker<span class="leader"></span>g</li>
      <li>Ballaststoffe<span class="leader"></span>g</li>
      <li>Eiweiß<span class="leader"></span>g</li>
      <li>Salz<span class="leader"></span>g</li>
    </ul>
    <p class="company">Plant Grillhouse GmbH</p>
  </section>

  <div class="divider"></div>
  <footer class="brand-band">
    <div class="brand"><span class="brand-dot"></span>PLANT GRILLHOUSE</div>
  </footer>
</main>
</body>
</html>
```